Ridgeline Outfitters Business Cards

Recently had a logo done with Artflockr and now looking for a business card to go along with it.

Target Market(s)

Ridgeline Outfitters is a weapons dealer. My market will be primarily men, hunting, shooting type.

Industry/Entity Type

Business

Contact Information for Business Card

I selected double sided, but this is not required, single or double is going to be fine. I picture the logo on one side, or perhaps just the circle which contains "RO" with the remaining info on the other side.

Font styles to use
Sans Serif

Requirements
Must have
• My name: Wesley Holm
• Title: Owner
• tel: 612-555-0378
• web: www.ridgelineoutfittersmn.example
Nice to have
• I like the concept of a black business card. I would like to keep the colors monotone, black, grey, white or red. Red is acceptable because it is in the logo. I have also seen cards that are matte black with shiny black as well, perhaps for the logo (or circle RO) part of the logo.
• I will upload a couple of the logos for use, and also an example I just found of the black on black. and some others that have a nice contrast.
Should not have
• lots of colors are not wanted.

```html
<!DOCTYPE html>
<html lang="en">
<head>
<meta charset="utf-8">
<title>Ridgeline Outfitters Business Card</title>
<link rel="stylesheet" href="https://fonts.googleapis.com/css2?family=Open+Sans:wght@400;600;700;800&display=swap">
<style>
  :root {
    --backdrop: #2e2e2f;
    --card: #19191a;
    --red: #d8261e;
    --grey: #6b6b6b;
    --white: #f4f4f4;
  }
  * { margin: 0; padding: 0; box-sizing: border-box; }
  html, body { width: 799px; height: 1200px; overflow: hidden; }
  body {
    background: var(--backdrop);
    font-family: "Open Sans", Arial, sans-serif;
    position: relative;
  }
  .card {
    position: absolute;
    left: 80px;
    width: 640px;
    height: 366px;
    background: var(--card);
    overflow: hidden;
    box-shadow: 0 14px 30px rgba(0,0,0,0.45);
  }
  .card--front { top: 117px; }
  .card--back { top: 717px; }

  /* Front */
  .brand {
    position: absolute;
    left: 0; right: 0; top: 0; bottom: 0;
    display: flex;
    align-items: center;
    justify-content: center;
    gap: 22px;
  }
  .brand__dot {
    width: 78px; height: 78px;
    border-radius: 50%;
    border: 7px solid var(--grey);
    flex: none;
  }
  .brand__name {
    color: var(--red);
    font-weight: 800;
    font-size: 30px;
    letter-spacing: 1px;
    text-transform: uppercase;
    line-height: 1.05;
  }

  /* Back */
  .contact {
    position: absolute;
    left: 34px;
    top: 24px;
    height: 250px;
    writing-mode: vertical-rl;
    transform: rotate(180deg);
    text-align: end;
    color: var(--white);
  }
  .contact__name {
    font-weight: 800;
    font-size: 22px;
    letter-spacing: -0.3px;
    text-transform: uppercase;
    line-height: 1.1;
  }
  .contact__title {
    color: var(--red);
    font-size: 12px;
    line-height: 1.1;
    margin-inline-start: 0;
  }
  .contact__line {
    font-size: 14px;
    line-height: 1.2;
    margin-left: 10px;
  }
  .contact__line--phone { margin-left: 18px; }
  .contact__icon {
    width: 11px; height: 11px;
    margin-block-start: 8px;
    vertical-align: middle;
  }
  .backmark {
    position: absolute;
    left: 260px;
    top: 125px;
    width: 440px;
    height: 440px;
    border-radius: 50%;
    border: 16px solid var(--grey);
  }
</style>
</head>
<body>
  <section class="card card--front">
    <div class="brand">
      <span class="brand__dot"></span>
      <span class="brand__name">Ridgeline<br>Outfitters</span>
    </div>
  </section>

  <section class="card card--back">
    <div class="contact">
      <div class="contact__name">Wesley Holm</div>
      <div class="contact__title">Owner</div>
      <div class="contact__line contact__line--phone">612-555-0378<svg class="contact__icon" viewBox="0 0 12 12" aria-hidden="true"><rect width="12" height="12" rx="2" fill="#f4f4f4"/><path d="M3.5 2.6c.4-.3.8-.2 1 .2l.6 1.2c.2.4.1.7-.2.9l-.5.4c.4.9 1.1 1.6 2 2l.4-.5c.2-.3.6-.4.9-.2l1.2.6c.4.2.5.6.2 1l-.6.7c-.4.4-1 .5-1.6.3C5 8.6 3.4 7 2.8 5.1c-.2-.6-.1-1.2.3-1.6z" fill="#19191a"/></svg></div>
      <div class="contact__line">www.ridgelineoutfittersmn.example<svg class="contact__icon" viewBox="0 0 12 12" aria-hidden="true"><circle cx="6" cy="6" r="5.6" fill="#f4f4f4"/><g fill="none" stroke="#19191a" stroke-width="0.8"><circle cx="6" cy="6" r="4.4"/><ellipse cx="6" cy="6" rx="2" ry="4.4"/><path d="M1.6 6h8.8M2.3 3.8h7.4M2.3 8.2h7.4"/></g></svg></div>
    </div>
    <span class="backmark"></span>
  </section>
</body>
</html>
```